Harrow's Electrical & Solar - Business Cards

I want my business card to stand out from the rest. I will provide my business name logo and my icon logo to be implemented onto the card.

On the front of the card, can i have the following. Just make it neat & professional please.

Liam Corbett
harrowselectrical@quillmail.test
0438 917 605
ABN: 41 602 719 384
License No. 582164K
FREE QUOTES
24/7 Emergency

On the back of the card, can I have "Our Services" and maybe add the S logo on the back in the background or something. Under "Our Services" I want the following:

LED Lighting Upgrades
Switches & Outlets
Smoke Alarms
Switchboard Upgrades
Fault Finding
Rewiring
New Builds
Test & Tagging
All Electrical Maintenance & Repairs

Can you guys add the instagram logo and next to it, put harrows_electrical

Can you guys also add the facebook logo and next to it put Harrow's Electrical & Solar. Make sure the instagram & facebook icon is in either white, green or black.

Also I have put down double sided, not sure why when i save it, it keeps going to single sided. I need my business card double sided.

Target Market(s)

New Customers

Contact Information for Business Card

Liam Corbett harrowselectrical@quillmail.test 0438 917 605 ABN: 41 602 719 384 License No. 582164K FREE QUOTES 24/7 Emergency

Requirements
Must have
• must be tidy, professional and appealing

```html
<!DOCTYPE html>
<html lang="en">
<head>
<meta charset="utf-8">
<title>Harrow's Electrical &amp; Solar – Business Cards</title>
<link rel="stylesheet" href="https://fonts.googleapis.com/css2?family=Audiowide&family=Lato:wght@400;700;900&display=swap">
<style>
  :root {
    --sheet: #cdcbcc;
    --card: #161616;
    --card-glow: #232323;
    --green: #22b33a;
    --green-dark: #1a9a30;
    --white: #ffffff;
    --text-soft: #e2e2e2;
    --rule: #a9a9a9;
    --tab: #b8bec5;
    --ink: #111111;
    --caption: #1a1a1a;
  }
  * { margin: 0; padding: 0; box-sizing: border-box; }
  html, body { width: 1200px; height: 893px; overflow: hidden; background: var(--sheet); }
  body { font-family: "Lato", sans-serif; position: relative; }

  .card {
    position: absolute; width: 420px; height: 240px;
    border-radius: 14px; overflow: hidden;
    background: radial-gradient(ellipse at 30% 55%, var(--card-glow) 0%, var(--card) 60%);
    box-shadow: 0 2px 5px rgba(0,0,0,.25);
    color: var(--white);
  }
  .card--front-1 { left: 156px; top: 153px; }
  .card--front-2 { left: 633px; top: 153px; }
  .card--front-3 { left: 156px; top: 460px; }
  .card--back    { left: 633px; top: 460px; background: var(--card); }

  .caption {
    position: absolute; width: 420px; text-align: center;
    font-weight: 700; font-size: 21px; letter-spacing: .5px; color: var(--caption);
  }

  /* front */
  .brand-name {
    position: absolute; left: 168px; top: 36px; width: 224px;
    text-align: center; font-family: "Lato", sans-serif; font-weight: 900;
    font-size: 20px; line-height: 21px; color: var(--green);
    text-transform: uppercase; letter-spacing: .5px;
  }
  .holder-name {
    position: absolute; left: 24px; top: 114px;
    font-family: "Audiowide", sans-serif; font-size: 19px; letter-spacing: 1px;
    color: var(--green); text-transform: uppercase;
  }
  .divider { position: absolute; left: 24px; top: 147px; width: 369px; height: 2px; background: var(--rule); }

  .contact { position: absolute; left: 24px; top: 159px; }
  .contact__row { display: flex; align-items: center; gap: 7px; height: 16px; }
  .contact__row svg { width: 8px; height: 8px; fill: var(--green); }
  .contact__phone { font-size: 12.5px; color: var(--text-soft); letter-spacing: .3px; }
  .contact__email { font-size: 10.5px; color: var(--text-soft); }

  .registration { position: absolute; left: 203px; top: 160px; font-size: 11px; line-height: 15px; color: var(--white); }
  .registration .label { color: var(--green); }

  .emergency { position: absolute; left: 340px; top: 158px; width: 54px; text-align: center; }
  .emergency__hours { font-weight: 900; font-size: 20px; line-height: 19px; letter-spacing: .5px; }
  .emergency__word { font-weight: 900; font-size: 7px; letter-spacing: .2px; }
  .emergency--accent .slash, .emergency--accent .emergency__word { color: var(--green); }
  .slash { font-style: italic; }

  .free-quotes { position: absolute; left: 24px; top: 198px; font-weight: 900; font-size: 12.5px; }
  .free-quotes span { color: var(--green); }

  .footer-band { position: absolute; left: 0; bottom: 0; width: 420px; height: 30px; }
  .social { position: absolute; left: 288px; top: 220px; display: flex; align-items: center; gap: 5px; font-size: 12px; color: var(--ink); }
  .social__dot { width: 11px; height: 11px; border-radius: 50%; background: var(--ink); }

  /* back */
  .emblem-area {
    position: absolute; left: 0; top: 0; width: 232px; height: 240px;
    background: linear-gradient(100deg, #f2f2f2 0%, #8a8a8a 30%, #3b3b3b 60%, var(--card) 100%);
    clip-path: polygon(0 0, 100% 0, 78% 100%, 0 100%);
  }
  .services-banner { position: absolute; right: 0; top: 22px; width: 187px; height: 26px; }
  .services-title {
    position: absolute; right: 12px; top: 26px;
    font-family: "Audiowide", sans-serif; font-size: 14.5px; letter-spacing: .8px;
    color: var(--ink); text-transform: uppercase;
  }
  .services { position: absolute; right: 18px; top: 57px; list-style: none; text-align: right; }
  .services li { font-size: 11.5px; line-height: 16.7px; color: var(--text-soft); display: flex; justify-content: flex-end; align-items: center; gap: 8px; }
  .services li .tick { width: 10px; height: 10px; flex: none; }
  .services li.continued { padding-right: 18px; }
</style>
</head>
<body>

<!-- Front variant 01 -->
<section class="card card--front-1">
  <div class="brand-name">Harrow's Electrical &amp; Solar</div>
  <div class="holder-name">Liam Corbett</div>
  <div class="divider"></div>
  <div class="contact">
    <div class="contact__row"><svg viewBox="0 0 10 10"><path d="M2 0h2l1 3-1.5 1a6 6 0 0 0 2.5 2.5L7 5l3 1v2a2 2 0 0 1-2 2A8 8 0 0 1 0 2a2 2 0 0 1 2-2z"/></svg><span class="contact__phone">0438 917 605</span></div>
    <div class="contact__row"><svg viewBox="0 0 10 10"><path d="M0 2h10v6H0z M0 2l5 3.5L10 2" stroke="#161616" stroke-width=".8"/></svg><span class="contact__email">harrowselectrical@quillmail.test</span></div>
  </div>
  <div class="registration"><div><span class="label">ABN:</span> 41 602 719 384</div><div><span class="label">Lic No.</span> 582164K</div></div>
  <div class="emergency"><div class="emergency__hours">24<span class="slash">/</span>7</div><div class="emergency__word">EMERGENCY</div></div>
  <div class="free-quotes">FREE <span>QUOTES</span></div>
  <svg class="footer-band" viewBox="0 0 420 30"><polygon points="0,19 262,19 256,30 0,30" fill="var(--green)"/><polygon points="278,0 420,0 420,30 264,30" fill="var(--tab)"/></svg>
  <div class="social"><span class="social__dot"></span><span>harrows_electrical</span></div>
</section>
<div class="caption" style="left:156px; top:410px;">FRONT CARD 01</div>

<!-- Front variant 02 -->
<section class="card card--front-2">
  <div class="brand-name">Harrow's Electrical &amp; Solar</div>
  <div class="holder-name">Liam Corbett</div>
  <div class="divider"></div>
  <div class="contact">
    <div class="contact__row"><svg viewBox="0 0 10 10"><path d="M2 0h2l1 3-1.5 1a6 6 0 0 0 2.5 2.5L7 5l3 1v2a2 2 0 0 1-2 2A8 8 0 0 1 0 2a2 2 0 0 1 2-2z"/></svg><span class="contact__phone">0438 917 605</span></div>
    <div class="contact__row"><svg viewBox="0 0 10 10"><path d="M0 2h10v6H0z M0 2l5 3.5L10 2" stroke="#161616" stroke-width=".8"/></svg><span class="contact__email">harrowselectrical@quillmail.test</span></div>
  </div>
  <div class="registration"><div><span class="label">ABN:</span> 41 602 719 384</div><div><span class="label">Lic No.</span> 582164K</div></div>
  <div class="emergency"><div class="emergency__hours">24<span class="slash">/</span>7</div><div class="emergency__word">EMERGENCY</div></div>
  <div class="free-quotes">FREE <span>QUOTES</span></div>
  <svg class="footer-band" viewBox="0 0 420 30"><polygon points="0,19 262,19 256,30 0,30" fill="var(--green)"/><polygon points="278,0 420,0 420,30 264,30" fill="var(--tab)"/></svg>
  <div class="social"><span class="social__dot"></span><span>harrows_electrical</span></div>
</section>
<div class="caption" style="left:633px; top:410px;">FRONT CARD 02</div>

<!-- Front variant 03 -->
<section class="card card--front-3">
  <div class="brand-name">Harrow's Electrical &amp; Solar</div>
  <div class="holder-name">Liam Corbett</div>
  <div class="divider"></div>
  <div class="contact">
    <div class="contact__row"><svg viewBox="0 0 10 10"><path d="M2 0h2l1 3-1.5 1a6 6 0 0 0 2.5 2.5L7 5l3 1v2a2 2 0 0 1-2 2A8 8 0 0 1 0 2a2 2 0 0 1 2-2z"/></svg><span class="contact__phone">0438 917 605</span></div>
    <div class="contact__row"><svg viewBox="0 0 10 10"><path d="M0 2h10v6H0z M0 2l5 3.5L10 2" stroke="#161616" stroke-width=".8"/></svg><span class="contact__email">harrowselectrical@quillmail.test</span></div>
  </div>
  <div class="registration"><div><span class="label">ABN:</span> 41 602 719 384</div><div><span class="label">Lic No.</span> 582164K</div></div>
  <div class="emergency emergency--accent"><div class="emergency__hours">24<span class="slash">/</span>7</div><div class="emergency__word">EMERGENCY</div></div>
  <div class="free-quotes">FREE <span>QUOTES</span></div>
  <svg class="footer-band" viewBox="0 0 420 30"><polygon points="0,19 262,19 256,30 0,30" fill="var(--green)"/><polygon points="278,0 420,0 420,30 264,30" fill="var(--tab)"/></svg>
  <div class="social"><span class="social__dot"></span><span>harrows_electrical</span></div>
</section>
<div class="caption" style="left:156px; top:714px;">FRONT CARD 03</div>

<!-- Back -->
<section class="card card--back">
  <div class="emblem-area" role="img" aria-label="Large brand emblem in a silver-to-black gradient"></div>
  <svg class="services-banner" viewBox="0 0 187 26"><polygon points="14,0 187,0 187,26 0,26" fill="var(--green)"/></svg>
  <div class="services-title">Our Services</div>
  <ul class="services">
    <li>LED Lighting Upgrades <svg class="tick" viewBox="0 0 10 10"><circle cx="5" cy="5" r="5" fill="var(--green)"/><path d="M2.8 5.2l1.5 1.5 3-3" stroke="#161616" stroke-width="1.3" fill="none"/></svg></li>
    <li>Switches &amp; Outlets <svg class="tick" viewBox="0 0 10 10"><circle cx="5" cy="5" r="5" fill="var(--green)"/><path d="M2.8 5.2l1.5 1.5 3-3" stroke="#161616" stroke-width="1.3" fill="none"/></svg></li>
    <li>Smoke Alarms <svg class="tick" viewBox="0 0 10 10"><circle cx="5" cy="5" r="5" fill="var(--green)"/><path d="M2.8 5.2l1.5 1.5 3-3" stroke="#161616" stroke-width="1.3" fill="none"/></svg></li>
    <li>Fault Finding <svg class="tick" viewBox="0 0 10 10"><circle cx="5" cy="5" r="5" fill="var(--green)"/><path d="M2.8 5.2l1.5 1.5 3-3" stroke="#161616" stroke-width="1.3" fill="none"/></svg></li>
    <li>Rewiring <svg class="tick" viewBox="0 0 10 10"><circle cx="5" cy="5" r="5" fill="var(--green)"/><path d="M2.8 5.2l1.5 1.5 3-3" stroke="#161616" stroke-width="1.3" fill="none"/></svg></li>
    <li>Switchboard Upgrades <svg class="tick" viewBox="0 0 10 10"><circle cx="5" cy="5" r="5" fill="var(--green)"/><path d="M2.8 5.2l1.5 1.5 3-3" stroke="#161616" stroke-width="1.3" fill="none"/></svg></li>
    <li>New Builds <svg class="tick" viewBox="0 0 10 10"><circle cx="5" cy="5" r="5" fill="var(--green)"/><path d="M2.8 5.2l1.5 1.5 3-3" stroke="#161616" stroke-width="1.3" fill="none"/></svg></li>
    <li>Test &amp; Tagging <svg class="tick" viewBox="0 0 10 10"><circle cx="5" cy="5" r="5" fill="var(--green)"/><path d="M2.8 5.2l1.5 1.5 3-3" stroke="#161616" stroke-width="1.3" fill="none"/></svg></li>
    <li>All Electrical Maintenance <svg class="tick" viewBox="0 0 10 10"><circle cx="5" cy="5" r="5" fill="var(--green)"/><path d="M2.8 5.2l1.5 1.5 3-3" stroke="#161616" stroke-width="1.3" fill="none"/></svg></li>
    <li class="continued">&amp; Repairs</li>
  </ul>
</section>
<div class="caption" style="left:620px; top:714px;">BACK CARD 01</div>

</body>
</html>
```